Broadcaster,Conference Host,Facilitator

Looking for a business card and logo to create the Grant Felber brand .. Something with a slant towards radio and conference speaking
I like the idea of classic black white or grey but open to suggestions

Target Market(s)

Corporates

Industry/Entity Type

Business

Contact Information for Business Card

Grant Felber
Email : Grant.Felber@quorvamail.co.uk
Mobile : +44 7700 382046
Twitter : @Grantfelber

Font styles to use
Serif
Decorative
Script

Requirements
Must have
• Feel classy and dynamic
Should not have
• Cartoons

```html
<!DOCTYPE html>
<html lang="en">
<head>
<meta charset="utf-8">
<title>Grant Felber — Business Card</title>
<link rel="stylesheet" href="https://fonts.googleapis.com/css2?family=Josefin+Sans:wght@400&family=Ubuntu:wght@400&display=swap">
<style>
  :root {
    --page: #ecebe8;
    --card: #fbfbfa;
    --band: #8b8b8e;
    --band-light: #9a9a9d;
    --ink: #1e1e1e;
    --name: #ffffff;
    --mic-light-a: #e4e4e4;
    --mic-light-b: #c4c4c4;
    --mic-cut-a: #6f6f72;
    --mic-cut-b: #a3a3a6;
  }
  * { box-sizing: border-box; margin: 0; padding: 0; }
  html, body { width: 1200px; height: 880px; overflow: hidden; }
  body {
    background: var(--page);
    display: flex;
    align-items: center;
    justify-content: center;
    gap: 40px;
  }
  .card {
    position: relative;
    width: 560px;
    height: 320px;
    background: var(--card);
    box-shadow: 0 10px 28px rgba(0,0,0,.16), 0 2px 6px rgba(0,0,0,.08);
    overflow: hidden;
  }
  /* Front */
  .card-front .accent-block {
    position: absolute;
    left: 0;
    top: 74px;
    width: 170px;
    height: 52px;
    background: var(--band-light);
  }
  .card-front .mic-emboss {
    position: absolute;
    left: 176px;
    top: 34px;
    width: 108px;
    height: 250px;
    border-radius: 40px 40px 20px 20px;
    background: linear-gradient(160deg, var(--mic-light-a), var(--mic-light-b));
  }
  .card-front .name-band {
    position: absolute;
    left: 300px;
    right: 0;
    top: 150px;
    height: 58px;
    background: var(--band);
    display: flex;
    align-items: center;
    padding-left: 16px;
  }
  .card-front .name {
    font-family: "Josefin Sans", sans-serif;
    font-weight: 400;
    font-variant: small-caps;
    font-size: 30px;
    letter-spacing: 1.5px;
    color: var(--name);
    white-space: nowrap;
  }
  /* Back */
  .card-back .contact {
    position: absolute;
    left: 92px;
    top: 62px;
    font-family: "Ubuntu", sans-serif;
    font-size: 14px;
    line-height: 1.45;
    color: var(--ink);
    list-style: none;
  }
  .card-back .contact li:nth-child(2) { padding-left: 10px; }
  .card-back .contact li:nth-child(3) { padding-left: 14px; }
  .card-back .mic-cutout {
    position: absolute;
    right: 56px;
    bottom: 30px;
    width: 150px;
    height: 150px;
    border-radius: 34px 34px 18px 40px;
    background: linear-gradient(150deg, var(--mic-cut-a), var(--mic-cut-b));
    box-shadow: inset 0 3px 8px rgba(0,0,0,.25);
  }
</style>
</head>
<body>
  <section class="card card-front" aria-label="Card front">
    <div class="accent-block"></div>
    <div class="mic-emboss" role="img" aria-label="Embossed vintage studio microphone illustration"></div>
    <div class="name-band">
      <span class="name">GrantFelber</span>
    </div>
  </section>

  <section class="card card-back" aria-label="Card back">
    <ul class="contact">
      <li>Email : Grant.Felber@quorvamail.co.uk</li>
      <li>Mobile : +44 7700 382046</li>
      <li>Twitter : @Grantfelber</li>
    </ul>
    <div class="mic-cutout" role="img" aria-label="Die-cut vintage microphone illustration"></div>
  </section>
</body>
</html>
```